Design Our Holiday Magic Coupon

Purpose - The purpose of this project is to create a festive, uplifting, and visually engaging physical coupon that will be mailed to our existing community and warm leads.
The intent is twofold: first, to spark delight and connection by offering a tangible, personal touch during the holiday season; and second, to encourage customers to explore and purchase our programs as they prepare for a strong start to 2026. This mailer is designed to re-engage past buyers, inspire current participants, and gently invite new momentum into their practice through a simple, friendly offer.

Project Description + Scope

This project includes the design and production of a printed coupon ( card format) featuring a 20% discount on purchases of $79 or more. The copy should feel warm, clear, and celebratory without urgency or pressure.

The front of the card will include the headline (“Live Your Best 2026”), bold discount information, and the coupon code JOLLYDAY20. The back will include a short message reinforcing the tone of possibility and ease, plus simple redemption instructions and the expiry date: December 31, 2025. Deliverables include print-ready artwork, color selection aligned with KH brand style.

one side
LIVE YOUR BEST 2026
Enjoy 20% OFF when you buy $79 or more.
Use code: JOLLYDAY20
Redeem until end of day December 31, 2025.

Back side - Move with clarity.
Heal with intelligence.
Lead with ease.
Thank you for being part of Kinetic Harmony.
Lots of love, Marla and the whole of Team Marla

Target Market(s)

yoga teachers, yoga lovers, mostly over 50 years, women

Font styles to use
Other font styles liked:
• see attached for feel

Colors
0054AA
0677BA
7BADD7
CADEEF
E8F1F8
0094D4
00A9DD
6FCCEA
C7EBF8
E9F6FB
00AB8E
00BBA5
67D7C9
C6EFE9
E9F9F6
EB3D1F
EC4F4E
F09395
F8D3D4
FCEDEE

Requirements
Nice to have
• see attached

```html
<!DOCTYPE html>
<html lang="en">
<head>
<meta charset="utf-8">
<title>Kinetic Harmony – Holiday Coupon</title>
<link rel="stylesheet" href="https://fonts.googleapis.com/css2?family=Arimo:wght@400;700&family=Cinzel:wght@500;600;700&display=swap">
<style>
  :root {
    --slate: #525560;
    --navy: #1b2a5a;
    --brand-violet: #3f3a86;
    --brand-blue: #0094d4;
    --band-blue: #0485c5;
    --bar-blue: #1a8fcc;
    --sky-deep: #5aa6d8;
    --sky-mid: #7badd7;
    --sky-pale: #cadeef;
    --mist: #e8f1f8;
    --white: #ffffff;
    --serif: "Cinzel", "Times New Roman", serif;
    --sans: "Arimo", Arial, sans-serif;
  }
  * { box-sizing: border-box; margin: 0; padding: 0; }
  html, body { width: 927px; height: 1200px; overflow: hidden; }
  body { background: var(--slate); position: relative; font-family: var(--sans); }

  .card {
    position: absolute; left: 88px; width: 750px; height: 413px; overflow: hidden;
    box-shadow: 6px 8px 10px rgba(0,0,0,.35);
  }
  .card--front {
    top: 121px;
    background: radial-gradient(ellipse 70% 90% at 18% 18%, var(--mist) 0%, var(--sky-pale) 40%, var(--sky-mid) 80%, var(--sky-deep) 100%);
  }
  .card--back {
    top: 663px;
    background: radial-gradient(ellipse 60% 80% at 85% 95%, var(--mist) 0%, var(--sky-pale) 30%, var(--sky-mid) 65%, var(--sky-deep) 100%);
  }

  /* brand lockup */
  .brand { position: absolute; display: flex; align-items: center; gap: 14px; }
  .brand__dot { width: 40px; height: 40px; border-radius: 50%; background: var(--brand-blue); }
  .brand__name { font-family: var(--sans); font-weight: 400; font-size: 26px; line-height: 25px; color: var(--brand-violet); }
  .card--front .brand { left: 48px; top: 44px; }
  .card--back .brand { right: 52px; top: 318px; }

  /* front */
  .headline { position: absolute; left: 48px; top: 140px; font-family: var(--serif); color: var(--navy); }
  .headline__lead { font-size: 31px; font-weight: 600; letter-spacing: .5px; display: block; }
  .headline__year { font-size: 114px; font-weight: 600; color: var(--brand-blue); line-height: 1; display: block; margin-top: -6px; letter-spacing: -1px; }

  .fireworks { position: absolute; border-radius: 50%; }
  .fireworks--front { left: 335px; top: 14px; width: 240px; height: 370px;
    background: radial-gradient(ellipse at 50% 35%, rgba(255,255,255,.55) 0%, rgba(123,173,215,.25) 55%, rgba(123,173,215,0) 75%); }

  .redeem { position: absolute; left: 48px; top: 355px; height: 30px; display: flex; align-items: stretch; }
  .redeem__note { background: var(--bar-blue); color: var(--white); font-size: 11.5px; border-radius: 15px 0 0 15px; padding: 0 8px 0 12px; display: flex; align-items: center; width: 337px; }
  .redeem__code { background: var(--navy); color: var(--white); font-size: 21px; font-weight: 400; letter-spacing: .2px; border-radius: 0 15px 15px 0; padding: 0 12px 0 10px; display: flex; align-items: center; width: 146px; }

  .offer-band { position: absolute; right: 0; top: 0; width: 172px; height: 413px; background: var(--band-blue); }
  .offer { position: absolute; left: -120.5px; top: 120.5px; width: 413px; height: 172px;
    transform: rotate(-90deg); padding: 20px 0 0 39px; color: var(--white); overflow: hidden; }
  .offer__enjoy { display: block; font-family: var(--serif); font-size: 19px; font-weight: 600; line-height: 20px; }
  .offer__amount { display: inline-block; font-family: var(--serif); font-size: 74px; font-weight: 600;
    line-height: 66px; white-space: nowrap; transform: scaleX(.82); transform-origin: left center; }
  .offer__terms { display: block; font-family: var(--sans); font-size: 27px; line-height: 30px; margin-top: 4px; white-space: nowrap; }

  /* back */
  .side-band { position: absolute; left: 0; top: 0; width: 171px; height: 413px; background: var(--band-blue); }
  .fireworks--back { left: 14px; top: 20px; width: 143px; height: 370px;
    background: radial-gradient(ellipse at 50% 40%, rgba(111,204,234,.45) 0%, rgba(111,204,234,.12) 60%, rgba(111,204,234,0) 80%); }

  .message { position: absolute; right: 42px; top: 33px; text-align: right; }
  .message__mantra { font-family: var(--serif); font-size: 39px; font-weight: 600; color: var(--white); line-height: 47px; }
  .message__thanks { font-family: var(--sans); font-size: 22px; color: var(--navy); margin-top: 14px; }
  .message__signoff { font-family: var(--serif); font-size: 18px; font-weight: 500; color: var(--navy); line-height: 25px; margin-top: 16px; }
</style>
</head>
<body>

<section class="card card--front" aria-label="Coupon front">
  <div class="brand">
    <span class="brand__dot"></span>
    <span class="brand__name">kinetic<br>harmony</span>
  </div>

  <h1 class="headline">
    <span class="headline__lead">LIVE YOUR BEST</span>
    <span class="headline__year">2026</span>
  </h1>

  <div class="fireworks fireworks--front" role="img" aria-label="Illustration of white and blue fireworks bursting"></div>

  <div class="redeem">
    <span class="redeem__note">Redeem until end of day December 31, 2025. Use code:</span>
    <span class="redeem__code">JOLLYDAY20</span>
  </div>

  <div class="offer-band">
    <div class="offer">
      <span class="offer__enjoy">ENJOY</span>
      <span class="offer__amount">20% OFF</span>
      <span class="offer__terms">when you buy $79 or more</span>
    </div>
  </div>
</section>

<section class="card card--back" aria-label="Coupon back">
  <div class="side-band">
    <div class="fireworks fireworks--back" role="img" aria-label="Illustration of fireworks and four-point sparkles"></div>
  </div>

  <div class="message">
    <p class="message__mantra">Move with clarity.<br>Heal with intelligence.<br>Lead with ease.</p>
    <p class="message__thanks">Thank you for being part of Kinetic Harmony.</p>
    <p class="message__signoff">Lots of love,<br>Marla and all of us at Kinetic Harmony.</p>
  </div>

  <div class="brand">
    <span class="brand__dot"></span>
    <span class="brand__name">kinetic<br>harmony</span>
  </div>
</section>

</body>
</html>
```